Rebrand of 3 bottle labels for nail polish brand

The task is to make a rebranding of our current gel nail polish bottle design. We have become one of the leading european nail polish brand, so we want to improve the quality of the label design to a more scandinavian and minimalistic bottle design, which stille has to be recognisable and unique.

We have attached a more detailed description of the rebranding instructions for our gel polish bottles called "bottle task".
Updates

The Labels should not be just Black and White as stated. But should be mainly Black and White and then some of our color as explained in the uploaded file.

Target Market(s)

Girls and women age 18-55 Northern Europe

Industry/Entity Type

Cosmetic/ Nail Gel Polish

Colors

Designer to choose only greyscale colors for use in the design.

Requirements
Must have
• See attched design instruction
Nice to have
• Moderne, Minimalist, Recognizable and Unique look
Should not have
• Too many elements, too busy design

```html
<!DOCTYPE html>
<html lang="en">
<head>
<meta charset="utf-8">
<title>Lumevo Color Coat – Label Set</title>
<link href="https://fonts.googleapis.com/css2?family=Josefin+Sans:wght@300;400&family=Marcellus&family=Archivo:wght@600&family=Roboto+Condensed:wght@400;700&family=Great+Vibes&display=swap" rel="stylesheet">
<style>
  :root {
    --backdrop: #e8e8ea;
    --label-black: #141414;
    --label-edge: #222222;
    --ink-white: #f2f2f2;
    --ink-soft: #b9b9b9;
    --ink-body: #8c8c8c;
    --ink-faint: #4a4a4a;
    --shade-taupe: #9a8279;
    --shade-ink: #1a1a1a;
    --hazard-red: #c8202a;
  }
  html, body {
    margin: 0;
    padding: 0;
    width: 1200px;
    height: 1200px;
    overflow: hidden;
    background: var(--backdrop);
  }
  .stage {
    width: 1200px;
    height: 1200px;
    display: flex;
    align-items: center;
    justify-content: center;
    gap: 20px;
  }
  .label {
    position: relative;
    flex: 0 0 370px;
    width: 370px;
    height: 400px;
    background: linear-gradient(90deg, var(--label-black), var(--label-edge) 50%, var(--label-black));
    border-radius: 8px;
    color: var(--ink-white);
    overflow: hidden;
  }

  /* back label */
  .back__text {
    position: absolute;
    left: 22px;
    top: 48px;
    width: 200px;
    font-family: "Roboto Condensed", sans-serif;
    font-weight: 400;
    font-size: 11px;
    line-height: 1.5;
    color: var(--ink-body);
    text-align: justify;
  }
  .back__text p { margin: 0 0 14px; }
  .back__icons {
    position: absolute;
    left: 240px;
    top: 48px;
    width: 64px;
    height: 300px;
  }
  .back__legal {
    position: absolute;
    left: 340px;
    top: 200px;
    transform: translate(-50%, -50%) rotate(90deg);
    font-family: "Roboto Condensed", sans-serif;
    font-size: 10px;
    letter-spacing: 0.5px;
    color: var(--ink-body);
    white-space: nowrap;
  }

  /* front label */
  .front__volume {
    position: absolute;
    left: 24px;
    top: 210px;
    transform: translate(-50%, -50%) rotate(-90deg);
    font-family: "Josefin Sans", sans-serif;
    font-weight: 300;
    font-size: 12px;
    letter-spacing: 1.5px;
    color: var(--ink-soft);
    white-space: nowrap;
  }
  .front__brand,
  .front__product,
  .front__cure,
  .front__dots {
    position: absolute;
    left: 20px;
    right: 70px;
    text-align: center;
  }
  .front__brand {
    top: 62px;
    font-family: "Josefin Sans", sans-serif;
    font-weight: 300;
    font-size: 44px;
  }
  .front__brand sup {
    font-size: 9px;
    vertical-align: 28px;
    margin-left: 1px;
  }
  .front__product {
    top: 162px;
    font-family: "Marcellus", serif;
    font-size: 31px;
    letter-spacing: 0.5px;
  }
  .front__cure {
    top: 208px;
    font-family: "Josefin Sans", sans-serif;
    font-weight: 300;
    font-size: 14px;
    letter-spacing: 3px;
    color: var(--ink-soft);
  }
  .front__dots {
    top: 248px;
    display: flex;
    justify-content: center;
    gap: 6px;
  }
  .front__dots span {
    width: 5px;
    height: 5px;
    border-radius: 50%;
    background: var(--ink-white);
  }
  .front__emblem {
    position: absolute;
    left: 50px;
    top: 262px;
    width: 100px;
    height: 100px;
  }
  .front__claim {
    position: absolute;
    left: 108px;
    top: 300px;
    font-family: "Great Vibes", cursive;
    font-size: 34px;
    color: var(--ink-white);
    white-space: nowrap;
  }
  .front__shade {
    position: absolute;
    right: 22px;
    top: 66px;
    width: 40px;
    height: 262px;
    background: var(--shade-taupe);
    display: flex;
    align-items: center;
    justify-content: center;
  }
  .front__shade-name {
    transform: rotate(-90deg);
    font-family: "Archivo", sans-serif;
    font-weight: 600;
    font-size: 22px;
    letter-spacing: 0.5px;
    color: var(--shade-ink);
    white-space: nowrap;
  }
  .front__number {
    position: absolute;
    right: 14px;
    top: 336px;
    width: 56px;
    text-align: center;
    font-family: "Roboto Condensed", sans-serif;
    font-weight: 700;
    font-size: 34px;
    color: var(--ink-white);
  }
</style>
</head>
<body>
  <main class="stage">

    <section class="label back">
      <div class="back__text">
        <p>Apply Color Coat after base coat and cure under lamp.</p>
        <p>Cure each thin layer for sixty seconds under LED light.</p>
        <p>Keep out of reach of children. Avoid contact with skin and eyes.</p>
        <p>If irritation occurs, stop use and rinse well with water.</p>
        <p>Contains acrylates, photoinitiator, pigments and stabilisers. Store cool.</p>
      </div>
      <svg class="back__icons" viewBox="0 0 64 300" aria-hidden="true">
        <!-- hazard diamond -->
        <rect x="12" y="6" width="40" height="40" transform="rotate(45 32 26)" fill="#ffffff" stroke="var(--hazard-red)" stroke-width="4"/>
        <rect x="30" y="13" width="4" height="17" fill="#111"/>
        <circle cx="32" cy="36" r="2.6" fill="#111"/>
        <!-- brush and jar -->
        <line x1="22" y1="92" x2="52" y2="76" stroke="var(--ink-soft)" stroke-width="2.5" stroke-linecap="round"/>
        <rect x="16" y="100" width="32" height="20" rx="4" fill="none" stroke="var(--ink-soft)" stroke-width="2"/>
        <line x1="16" y1="107" x2="48" y2="107" stroke="var(--ink-soft)" stroke-width="1.5"/>
        <!-- recycle -->
        <circle cx="32" cy="168" r="16" fill="none" stroke="#ffffff" stroke-width="4" stroke-dasharray="22 11"/>
        <polygon points="44,150 50,160 40,160" fill="#ffffff"/>
        <polygon points="14,172 20,182 24,172" fill="#ffffff"/>
        <!-- lamp -->
        <path d="M14 250 Q14 222 32 222 Q50 222 50 250 Z" fill="none" stroke="var(--ink-soft)" stroke-width="2"/>
        <rect x="10" y="250" width="44" height="6" rx="2" fill="none" stroke="var(--ink-soft)" stroke-width="2"/>
      </svg>
      <div class="back__legal">Made in EU. Batch and expiry on base.</div>
    </section>

    <section class="label front">
      <div class="front__volume">15ml e 0.5oz</div>
      <div class="front__brand">lumevo<sup>TM</sup></div>
      <div class="front__product">COLOR COAT</div>
      <div class="front__cure">SOAK OFF UV/LED</div>
      <div class="front__dots"><span></span><span></span><span></span></div>
      <svg class="front__emblem" viewBox="0 0 100 100" role="img" aria-label="Faint leaf emblem decoration">
        <circle cx="50" cy="50" r="46" fill="var(--ink-faint)" opacity="0.35"/>
      </svg>
      <div class="front__claim">Vegan Formula</div>
      <div class="front__shade"><span class="front__shade-name">COLOR NAME</span></div>
      <div class="front__number">201</div>
    </section>

    <section class="label front">
      <div class="front__volume">15ml e 0.5oz</div>
      <div class="front__brand">lumevo<sup>TM</sup></div>
      <div class="front__product">COLOR COAT</div>
      <div class="front__cure">SOAK OFF UV/LED</div>
      <div class="front__dots"><span></span><span></span><span></span></div>
      <svg class="front__emblem" viewBox="0 0 100 100" role="img" aria-label="Faint leaf emblem decoration">
        <circle cx="50" cy="50" r="46" fill="var(--ink-faint)" opacity="0.35"/>
      </svg>
      <div class="front__claim">Vegan Formula</div>
      <div class="front__shade"><span class="front__shade-name">COLOR NAME</span></div>
      <div class="front__number">201</div>
    </section>

  </main>
</body>
</html>
```